I need a fresh looking, exciting and loaded design for Full service Restaurant

We need a web design for our restaurant, which offers full service Pakistani and Indian food in PA, USA. Design should be elegant, simplified so customers can navigate easily and order food online for catering as well as delivery. We need loads of pictures and room to grow. I already have a web address via tenvorahost.com. It should include SSL and e-commerce for ordering food.
Be original and be creative and make it a fun site :)

```html
<!DOCTYPE html>
<html lang="en">
<head>
<meta charset="utf-8">
<title>Saffron Lane – Indian &amp; Pakistani Kitchen</title>
<link rel="stylesheet" href="https://fonts.googleapis.com/css2?family=Open+Sans:wght@400;600;700&family=Raleway:wght@400;500;600;700&display=swap">
<style>
:root{
  --red:#d9232d;
  --red-dark:#b81d26;
  --ink:#222;
  --text:#555;
  --muted:#888;
  --line:#dcdcdc;
  --dark:#3a3a3a;
  --btn-dark:#4a4a4a;
  --paper:#fff;
  --soft:#f4f4f4;
  --news:#c9c9c9;
}
*{box-sizing:border-box;margin:0;padding:0}
html,body{width:1200px;height:2922px;overflow:hidden}
body{position:relative;background:var(--paper);font-family:"Open Sans",Arial,sans-serif;color:var(--text)}
.abs{position:absolute}
svg{display:block}

/* top navigation */
.topnav{left:0;top:0;width:1200px;height:68px;background:var(--paper)}
.topnav .links{left:62px;top:26px;display:flex;font-size:11px;color:#333;text-transform:uppercase}
.topnav .links span{padding:0 16px;border-left:1px solid #999;line-height:12px}
.topnav .links span:first-child{border-left:none;padding-left:0}
.search{left:600px;top:19px;display:flex}
.search .field{width:268px;height:32px;border:1px solid #ccc;font-size:11px;color:#aaa;padding:9px 12px}
.search .go{width:76px;height:32px;background:#333;color:#fff;font-size:11px;text-align:center;line-height:32px;text-transform:uppercase}
.locale{left:978px;top:26px;font-size:11px;color:#666;word-spacing:18px}
.cart{left:1095px;top:14px}
.cart .badge{position:absolute;left:22px;top:-2px;width:18px;height:18px;border-radius:50%;background:var(--red);color:#fff;font-size:10px;text-align:center;line-height:18px}

/* hero */
.hero{left:0;top:68px;width:1200px;height:649px;background:linear-gradient(110deg,#9c5b3c 0%,#c98a5a 30%,#8c3a22 60%,#d8914f 85%,#a45a30 100%)}
.brand-box{left:119px;top:164px;width:456px;height:434px;background:var(--paper);display:flex;align-items:center;justify-content:center;gap:14px}
.brand-box .dot{width:26px;height:26px;border-radius:50%;background:var(--red)}
.brand-box .name{font-family:"Raleway",sans-serif;font-weight:700;font-size:40px;color:#3b3b3b}
.order{left:575px;top:164px;width:483px;height:434px;background:rgba(255,255,255,.82)}
.order h2{position:absolute;left:0;width:483px;top:28px;text-align:center;font-family:"Raleway",sans-serif;font-weight:600;font-size:34px;color:var(--red)}
.select{position:absolute;left:64px;width:354px;height:32px;border:1px solid #bbb;background:rgba(255,255,255,.85);font-size:11px;color:#555;padding:8px 10px}
.select:after{content:"";position:absolute;right:10px;top:13px;border:4px solid transparent;border-top:5px solid #444}
.booking{position:absolute;left:64px;top:355px;width:354px;height:54px;background:var(--red);color:#fff;font-family:"Raleway",sans-serif;font-weight:600;font-size:28px;text-align:center;line-height:54px}

/* categories */
.tile{top:748px;width:458px;height:290px}
.tile.indian{left:142px;background:linear-gradient(135deg,#e9a3a0,#d98b7c 50%,#c9735f)}
.tile.pakistani{left:606px;background:linear-gradient(135deg,#d9a46a,#b76a3a 50%,#7d3a1e)}
.diamond{position:absolute;left:50%;top:50%;width:150px;height:150px;margin:-75px 0 0 -75px;background:var(--paper);transform:rotate(45deg);border-radius:10px}
.tile .label{position:absolute;left:0;right:0;top:50%;transform:translateY(-50%);text-align:center;font-family:"Raleway",sans-serif;font-weight:600;font-size:26px;line-height:28px;color:var(--red)}

/* specials */
.specials{left:0;top:1075px;width:1200px;height:425px;background:linear-gradient(100deg,#e8c84a 0%,#d9a860 25%,#7a5038 50%,#b46a38 75%,#8a3c1e 100%)}
.special-card{left:117px;top:1149px;width:949px;height:287px;background:rgba(255,255,255,.9)}
.special-card h2{position:absolute;left:0;width:949px;top:22px;text-align:center;font-family:"Raleway",sans-serif;font-weight:600;font-size:34px;color:var(--red)}
.special-img{position:absolute;left:88px;top:88px;width:187px;height:167px;background:radial-gradient(circle at 50% 45%,#f4e3a6,#e0c07a 45%,#8a5a34 80%)}
.special-text{position:absolute;left:301px;top:94px;width:560px}
.special-text h3{font-size:16px;font-weight:700;color:var(--ink);margin-bottom:8px}
.special-text p{font-size:11.5px;line-height:20px;color:#555}
.special-text .more{font-size:11.5px;color:var(--red);margin-top:4px}
.arrow{width:36px;height:36px;border-radius:50%;background:rgba(255,255,255,.45);top:1286px}

/* popular */
.popular{left:0;top:1500px;width:1200px;height:565px;background:var(--soft)}
.section-title{left:0;width:1200px;top:1538px;text-align:center;font-family:"Raleway",sans-serif;font-size:22px;letter-spacing:1px;color:var(--ink)}
.section-title b{color:var(--red);font-weight:500}
.title-rule{top:1551px;height:1px;background:var(--line)}
.sorts{left:960px;top:1536px;font-size:10px;color:#777;word-spacing:28px}
.sorts b{color:var(--red);font-weight:400}
.card{top:1603px;width:272px;height:433px;background:var(--soft);border:1px solid var(--line)}
.card.hover{background:#d9d9d9;border-color:#cfcfcf}
.card .sale{position:absolute;left:0;top:0;width:30px;height:16px;background:var(--red);color:#fff;font-size:9px;text-align:center;line-height:16px}
.card .photo{position:absolute;left:33px;top:20px;width:190px;height:190px}
.card .price{position:absolute;left:19px;top:222px;font-size:20px;color:var(--red)}
.card .qty{position:absolute;left:120px;top:227px;font-size:11px;color:#666}
.card .qty i{display:inline-block;font-style:normal;width:26px;height:22px;border:1px solid #ccc;background:#fff;text-align:center;line-height:20px;margin-left:10px}
.card .sep{position:absolute;left:0;right:0;top:268px;height:1px;background:var(--line)}
.card h4{position:absolute;left:19px;top:283px;font-weight:400;font-size:15px;color:#555}
.card p{position:absolute;left:19px;top:309px;width:235px;font-size:10.5px;line-height:17px;color:#888}
.card .btn{position:absolute;top:384px;height:46px;font-size:10px;font-weight:600;color:#fff;text-transform:uppercase;display:flex;align-items:center;justify-content:center;gap:7px}
.card .add{left:19px;width:130px;background:var(--red)}
.card .more{left:159px;width:95px;background:var(--btn-dark)}
.quick{position:absolute;left:52px;top:98px;width:136px;height:46px;background:rgba(40,40,40,.85);color:#fff;font-size:11px;text-transform:uppercase;display:flex;align-items:center;justify-content:center;gap:14px}

/* features */
.features{left:0;top:2065px;width:1200px;height:215px;display:flex}
.feature{flex:1;display:flex;flex-direction:column;align-items:center;padding-top:56px;border-left:1px solid #e6e6e6;font-size:16px;font-weight:600;color:#555;text-align:center;line-height:21px}
.feature:first-child{border-left:none}
.feature .ico{width:60px;height:60px;border-radius:50%;background:#777;display:flex;align-items:center;justify-content:center;margin-bottom:14px}
.feature.active{color:var(--red)}
.feature.active .ico{background:var(--red)}

/* newsletter */
.newsletter{left:0;top:2280px;width:1200px;height:208px;background:var(--news)}
.newsletter h2{position:absolute;right:720px;top:56px;font-family:"Raleway",sans-serif;font-weight:400;font-size:34px;color:var(--red);white-space:nowrap}
.newsletter p{position:absolute;right:720px;top:104px;width:440px;text-align:right;font-size:12px;line-height:20px;color:#333}
.news-field{position:absolute;left:518px;top:55px;width:247px;height:40px;background:#fff;font-size:11px;color:#aaa;padding:12px 20px}
.news-btn{position:absolute;left:518px;top:108px;width:247px;height:38px;background:#333;color:#fff;font-size:11px;text-align:center;line-height:38px;text-transform:uppercase}
.guarantee{position:absolute;left:799px;top:28px;width:356px;height:150px;background:var(--red);display:flex;align-items:center;gap:30px;padding-left:30px}
.guarantee .txt{font-family:"Open Sans",sans-serif;font-weight:700;font-size:38px;line-height:42px;color:#fff;letter-spacing:1px}

/* footer */
.footer{left:0;top:2488px;width:1200px;height:337px;background:var(--soft)}
.fcol{position:absolute;top:46px;height:260px}
.fcol h5{font-size:16px;font-weight:600;color:#444;margin-bottom:42px}
.fcol ul{list-style:none;font-size:11px;color:#777;text-transform:uppercase}
.fcol li{margin-bottom:21px}
.fcol.div{border-left:1px solid #e2e2e2;padding-left:0}
.contact{font-size:11px;color:#777;text-transform:uppercase;line-height:21px}
.contact .phone{font-size:22px;color:#222;text-transform:none;margin:2px 0 26px 36px}
.bottombar{left:0;top:2825px;width:1200px;height:97px;background:var(--dark)}
.bottombar .copy{position:absolute;left:56px;top:40px;font-size:12px;color:#ddd}
.social{position:absolute;left:930px;top:30px;display:flex;gap:12px}
.social span{width:40px;height:40px;border:1px solid #888;display:flex;align-items:center;justify-content:center}
.social span i{width:12px;height:12px;background:#fff}
.social span.on{background:var(--red);border-color:var(--red)}
</style>
</head>
<body>

<header class="topnav abs">
  <nav class="links abs"><span>Home</span><span>My Account</span><span>My Wishlist</span><span>Checkout</span><span>Register</span><span>Login</span></nav>
  <div class="search abs"><div class="field">Enter keyword</div><div class="go">Search</div></div>
  <div class="locale abs">EN&#9662; $&#9662;</div>
  <div class="cart abs">
    <svg width="44" height="40" viewBox="0 0 44 40"><path d="M4 16h36l-5 20H9z" fill="#333"/><path d="M14 16l6-10M30 16l-6-10" stroke="#333" stroke-width="3" fill="none"/><path d="M15 22v9M22 22v9M29 22v9" stroke="#fff" stroke-width="2"/></svg>
    <span class="badge">0</span>
  </div>
</header>

<section class="hero abs" role="img" aria-label="Street grill stall with kebab skewers, fried snacks and fresh food">
</section>
<div class="brand-box abs"><span class="dot"></span><span class="name">Saffron Lane</span></div>
<form class="order abs">
  <h2>ONLINE ORDER</h2>
  <div class="select" style="top:91px">Select Food Items</div>
  <div class="select" style="top:143px">Select Food</div>
  <div class="select" style="top:195px">Name</div>
  <div class="select" style="top:250px">Address</div>
  <div class="select" style="top:302px">Address</div>
  <div class="booking">BOOKING</div>
</form>

<div class="tile indian abs" role="img" aria-label="Indian thali platter with bowls of curries and sides">
  <div class="diamond"></div><div class="label">Indian Food<br>Items</div>
</div>
<div class="tile pakistani abs" role="img" aria-label="Pakistani naan bread with karahi curry dishes">
  <div class="diamond"></div><div class="label">Pakistani Food<br>Items</div>
</div>

<section class="specials abs" role="img" aria-label="Table spread of rice, naan bread and curries"></section>
<div class="special-card abs">
  <h2>TODAY SPECIAL FOOD ITEMS</h2>
  <div class="special-img" role="img" aria-label="Bowl of saffron basmati rice"></div>
  <div class="special-text">
    <h3>Lorem ipsum dolor sit amet, consectetur</h3>
    <p>Lorem ipsum dolor sit amet, consectetur adipiscing elit, sed do eiusmod tempor incididunt ut labore et dolore magna aliqua. Ut enim ad minim veniam, quis nostrud exercitation ullamco laboris nisi ut aliquip ex ea commodo consequat. Lorem ipsum dolor sit amet, consectetur adipiscing elit, sed do eiusmod tempor incididunt ut labore et dolore magna aliqua. Ut enim ad minim veniam, quis nostrud exercitation ullamco laboris.</p>
    <div class="more">Read More &#9656;</div>
  </div>
</div>
<div class="arrow abs" style="left:98px"><svg width="36" height="36"><path d="M21 11l-7 7 7 7" stroke="#fff" stroke-width="2.5" fill="none"/></svg></div>
<div class="arrow abs" style="left:1046px"><svg width="36" height="36"><path d="M15 11l7 7-7 7" stroke="#fff" stroke-width="2.5" fill="none"/></svg></div>

<section class="popular abs"></section>
<div class="title-rule abs" style="left:49px;width:440px"></div>
<div class="title-rule abs" style="left:712px;width:230px"></div>
<h2 class="section-title abs"><b>POPULAR</b>&nbsp; DISHES</h2>
<div class="sorts abs"><b>PRICE</b> CATEGORY BRAND</div>

<article class="card abs" style="left:49px">
  <span class="sale">25%</span>
  <div class="photo" role="img" aria-label="Grilled chicken with salad and tomatoes" style="background:linear-gradient(135deg,#f3efe6,#c8764a 55%,#8a3a22)"></div>
  <span class="price">$133.1</span><span class="qty">Quantity<i>1</i></span><span class="sep"></span>
  <h4>Name of Dishes</h4>
  <p>A slow-cooked house favourite with fresh herbs and warm spices.</p>
  <span class="btn add"><svg width="12" height="11"><path d="M0 1h2l2 7h7l1-5H3" stroke="#fff" stroke-width="1.5" fill="none"/></svg>Add to cart</span>
  <span class="btn more"><svg width="12" height="12"><circle cx="6" cy="6" r="5" stroke="#fff" fill="none" stroke-width="1.5"/></svg>More</span>
</article>
<article class="card hover abs" style="left:331px">
  <div class="photo" role="img" aria-label="Curry served in a copper pot" style="background:linear-gradient(135deg,#d8d0c4,#a88c70 55%,#6a5040)"></div>
  <span class="quick">Quick view <svg width="8" height="12"><path d="M1 1l5 5-5 5" stroke="#fff" stroke-width="2" fill="none"/></svg></span>
  <span class="price">$93.0</span><span class="qty">Quantity<i>1</i></span><span class="sep"></span>
  <h4>Name of Dishes</h4>
  <p>A slow-cooked house favourite with fresh herbs and warm spices.</p>
  <span class="btn add"><svg width="12" height="11"><path d="M0 1h2l2 7h7l1-5H3" stroke="#fff" stroke-width="1.5" fill="none"/></svg>Add to cart</span>
  <span class="btn more"><svg width="12" height="12"><circle cx="6" cy="6" r="5" stroke="#fff" fill="none" stroke-width="1.5"/></svg>More</span>
</article>
<article class="card abs" style="left:612px">
  <span class="sale">25%</span>
  <div class="photo" role="img" aria-label="Yellow potato curry in a copper bowl" style="background:radial-gradient(circle at 50% 55%,#f2c24a,#e0a030 45%,#b8682e 75%,#f3ece0)"></div>
  <span class="price">$68.8</span><span class="qty">Quantity<i>1</i></span><span class="sep"></span>
  <h4>Name of Dishes</h4>
  <p>A slow-cooked house favourite with fresh herbs and warm spices.</p>
  <span class="btn add"><svg width="12" height="11"><path d="M0 1h2l2 7h7l1-5H3" stroke="#fff" stroke-width="1.5" fill="none"/></svg>Add to cart</span>
  <span class="btn more"><svg width="12" height="12"><circle cx="6" cy="6" r="5" stroke="#fff" fill="none" stroke-width="1.5"/></svg>More</span>
</article>
<article class="card abs" style="left:892px">
  <div class="photo" role="img" aria-label="Red chicken curry in a serving dish" style="background:radial-gradient(circle at 50% 55%,#d9662e,#b8441c 50%,#6a3a22 80%)"></div>
  <span class="price">$33.1</span><span class="qty">Quantity<i>1</i></span><span class="sep"></span>
  <h4>Name of Dishes</h4>
  <p>A slow-cooked house favourite with fresh herbs and warm spices.</p>
  <span class="btn add"><svg width="12" height="11"><path d="M0 1h2l2 7h7l1-5H3" stroke="#fff" stroke-width="1.5" fill="none"/></svg>Add to cart</span>
  <span class="btn more"><svg width="12" height="12"><circle cx="6" cy="6" r="5" stroke="#fff" fill="none" stroke-width="1.5"/></svg>More</span>
</article>

<section class="features abs">
  <div class="feature active"><span class="ico"><svg width="24" height="26"><rect x="3" y="11" width="18" height="14" rx="2" fill="#fff"/><path d="M7 11V7a5 5 0 0 1 10 0" stroke="#fff" stroke-width="2.5" fill="none"/></svg></span>Secure payment</div>
  <div class="feature"><span class="ico"><svg width="28" height="20"><rect x="1" y="3" width="16" height="12" fill="#fff"/><path d="M17 7h6l4 4v4H17z" fill="#fff"/><circle cx="7" cy="17" r="2.5" fill="#fff"/><circle cx="22" cy="17" r="2.5" fill="#fff"/></svg></span>Free standard<br>shipping</div>
  <div class="feature"><span class="ico"><svg width="26" height="26"><path d="M21 9a9 9 0 0 0-16 1M5 17a9 9 0 0 0 16-1" stroke="#fff" stroke-width="2.5" fill="none"/><path d="M22 3v7h-7M4 23v-7h7" fill="#fff"/></svg></span>Fresh Food<br>Items</div>
  <div class="feature"><span class="ico"><svg width="24" height="24"><rect x="2" y="8" width="20" height="5" fill="#fff"/><rect x="4" y="14" width="16" height="9" fill="#fff"/><rect x="11" y="8" width="2" height="15" fill="#777"/><path d="M12 8c-2-6-8-5-5-1M12 8c2-6 8-5 5-1" stroke="#fff" stroke-width="2" fill="none"/></svg></span>Free gift box</div>
  <div class="feature"><span class="ico"><svg width="24" height="24"><circle cx="12" cy="7" r="5" fill="#fff"/><path d="M2 23a10 8 0 0 1 20 0z" fill="#fff"/></svg></span>Custermer<br>Support</div>
</section>

<section class="newsletter abs">
  <h2>Newsletter Sign Up</h2>
  <p>Lorem ipsum dolor sit amet conse ctetur adipiscing elit, sed do eiusmod tempor incididunt ut labore et dolore magna aliqua.</p>
  <div class="news-field">Enter your Email Address</div>
  <div class="news-btn">Subscribe</div>
  <div class="guarantee">
    <svg width="52" height="52" viewBox="0 0 52 52"><rect x="4" y="22" width="10" height="24" fill="#fff"/><path d="M18 22l10-16c4 0 6 3 5 7l-2 8h13c3 0 5 3 4 6l-4 15c-1 3-3 4-6 4H18z" fill="#fff"/></svg>
    <div class="txt">100 %<br>GUARANTEEN</div>
  </div>
</section>

<footer class="footer abs">
  <div class="fcol" style="left:53px"><h5>Information</h5><ul><li>About Us</li><li>Delivery Information</li><li>Privacy Policy</li><li>Terms &amp; Conditions</li></ul></div>
  <div class="fcol div" style="left:262px;padding-left:20px"><h5>Customer Service</h5><ul><li>Contact Us</li><li>Returns</li><li>Site Map</li><li>Forget Password</li></ul></div>
  <div class="fcol div" style="left:487px;padding-left:18px"><h5>Extras</h5><ul><li>Brands</li><li>Gift Vouchers</li><li>Affiliates</li><li>Specials</li></ul></div>
  <div class="fcol div" style="left:708px;padding-left:18px"><h5>My Account</h5><ul><li>My Account</li><li>Order History</li><li>Wish List</li><li>Newsletter</li></ul></div>
  <div class="fcol div" style="left:948px;padding-left:18px;width:230px">
    <h5 style="margin-bottom:30px">Contact Us</h5>
    <div class="contact">My Company , Address Line1,<br>Address Line2, Country -123456<br><br>Call us now toll free:
      <div class="phone">0100-555-0147</div>Email:<br>info@saffronlane-kitchen.org</div>
  </div>
</footer>

<div class="bottombar abs">
  <div class="copy">All Right Reserved. Copyrights @2016</div>
  <div class="social"><span><i></i></span><span><i></i></span><span><i></i></span><span class="on"><i></i></span><span><i></i></span></div>
</div>

</body>
</html>
```